Harbor Nightclub

Nightclub flyer., digital single sided, for KV and PX. I included samples of some previous flyers we've used. Sample Info:
HARBOR
FRIDAYS
FRI MAY 1 2020
DJ VORTAN (club floor)
DJ RUZO & DJ TAV (residents on the lounge floor)
4217 Marlow Avenue Sacramento
www.harborvenuehall.example for list/VIP inquiries

Target Market(s)

Upscale top 40 crowd but want some cool and artsy like the examples included.

Font styles to use
Sans Serif

Requirements
Must have
• Harbor Logo
Nice to have
• Would be nice if the flyer can be incorporated later with DJ photos (sometimes we will add dj photos to pixagram etc). Would like a big city type of feel.
Should not have
• Nothing too sexual.

```html
<!DOCTYPE html>
<html lang="en">
<head>
<meta charset="utf-8">
<title>Harbor Nightclub – Friday</title>
<link rel="stylesheet" href="https://fonts.googleapis.com/css2?family=Bodoni+Moda:wght@500;600;700&family=Arimo:wght@700&display=swap">
<style>
  :root {
    --magenta: #c8205e;
    --violet: #4a1e4a;
    --night: #120c18;
    --teal: #1d4f5c;
    --navy: #0f3c6b;
    --ember: #c2460f;
    --olive: #8b8a2a;
    --olive-soft: #a8a955;
    --sage: #9fb58a;
    --cream: #f3efd6;
    --white: #ffffff;
  }
  * { margin: 0; padding: 0; box-sizing: border-box; }
  html, body { width: 960px; height: 1200px; overflow: hidden; background: var(--night); }
  .flyer {
    position: relative;
    width: 960px;
    height: 1200px;
    overflow: hidden;
    font-family: "Bodoni Moda", "Didot", serif;
    color: var(--white);
  }
  .street-scene {
    position: absolute; inset: 0;
    background:
      radial-gradient(ellipse 420px 300px at 150px 780px, rgba(194,70,15,0.75), transparent 70%),
      radial-gradient(ellipse 360px 260px at 880px 260px, rgba(40,110,110,0.55), transparent 70%),
      radial-gradient(ellipse 500px 400px at 480px 560px, rgba(10,8,14,0.85), transparent 75%),
      linear-gradient(100deg, var(--magenta) 0%, var(--violet) 35%, var(--night) 55%, var(--teal) 78%, var(--navy) 100%);
  }
  .accent-lines { position: absolute; inset: 0; }
  .headline {
    position: absolute; left: 0; width: 960px; top: 212px;
    text-align: center;
    font-size: 150px; font-weight: 600; line-height: 1;
    letter-spacing: 14px; padding-left: 14px;
  }
  .date-band {
    position: absolute; left: 209px; top: 375px; width: 518px; height: 39px;
    background: var(--olive);
    color: var(--cream);
    font-size: 30px; font-weight: 700; line-height: 39px;
    text-align: center; letter-spacing: 10px;
  }
  .venue-mark {
    position: absolute; left: 0; width: 960px; top: 495px;
    display: flex; flex-direction: column; align-items: center;
  }
  .venue-dot { width: 90px; height: 90px; border-radius: 50%; background: var(--olive-soft); }
  .venue-name { margin-top: 22px; font-size: 44px; font-weight: 500; letter-spacing: 1px; line-height: 1; }
  .dj-photo { position: absolute; border-radius: 4px; }
  .dj-photo--club {
    left: 100px; top: 660px; width: 187px; height: 293px;
    background: linear-gradient(180deg, rgba(70,40,35,0.9), rgba(40,25,25,0.95));
  }
  .dj-photo--lounge {
    left: 420px; top: 657px; width: 510px; height: 290px;
    background: linear-gradient(90deg, rgba(40,35,60,0.85), rgba(60,75,95,0.9));
  }
  .lineup { position: absolute; top: 955px; text-align: center; }
  .lineup--club { left: 61px; width: 304px; }
  .lineup--lounge { left: 511px; width: 389px; }
  .lineup-name {
    border-top: 1px solid var(--white); border-bottom: 1px solid var(--white);
    font-size: 40px; font-weight: 500; line-height: 46px; white-space: nowrap;
  }
  .lineup-floor {
    margin-top: 9px;
    font-family: "Arimo", "Arial", sans-serif; font-weight: 700;
    font-size: 19px; letter-spacing: 0.3px;
  }
  .address-band {
    position: absolute; left: 0; top: 1067px; width: 960px; height: 48px;
    background: linear-gradient(90deg, var(--olive) 0%, var(--olive-soft) 60%, var(--sage) 100%);
    color: var(--cream);
    font-size: 22px; font-weight: 700; line-height: 48px;
    text-align: center; letter-spacing: 11px;
  }
  .contact {
    position: absolute; left: 0; width: 960px; top: 1130px;
    text-align: center;
    font-family: "Arimo", "Arial", sans-serif; font-weight: 700;
    font-size: 19px; line-height: 27px;
  }
</style>
</head>
<body>
<main class="flyer">
  <div class="street-scene" role="img" aria-label="Night street outside the club with a crowd, street lamps and an orange sports car, tinted magenta to teal"></div>

  <svg class="accent-lines" width="960" height="1200" viewBox="0 0 960 1200" aria-hidden="true">
    <polygon points="283,145 560,195 340,470" fill="none" stroke="#e88aa0" stroke-opacity="0.6" stroke-width="6"/>
    <polygon points="300,160 820,230 520,500" fill="none" stroke="#7ad0c4" stroke-opacity="0.35" stroke-width="5"/>
  </svg>

  <h1 class="headline">FRIDAY</h1>
  <div class="date-band">FRI MAY 1, 2020</div>

  <div class="venue-mark">
    <div class="venue-dot"></div>
    <div class="venue-name">HARBOR</div>
  </div>

  <div class="dj-photo dj-photo--club" role="img" aria-label="Photo of DJ Vortan wearing headphones"></div>
  <div class="dj-photo dj-photo--lounge" role="img" aria-label="Photo of DJ Ruzo and DJ Tav wearing headphones"></div>

  <div class="lineup lineup--club">
    <div class="lineup-name">DJ VORTAN</div>
    <div class="lineup-floor">CLUB FLOOR</div>
  </div>
  <div class="lineup lineup--lounge">
    <div class="lineup-name">DJ RUZO &amp; DJ TAV</div>
    <div class="lineup-floor">RESIDENTS ON THE LOUNGE FLOOR</div>
  </div>

  <div class="address-band">4217 MARLOW AVENUE SACRAMENTO</div>

  <div class="contact">
    <div>www.harborvenuehall.example</div>
    <div>For List/VIP Inquiries</div>
  </div>
</main>
</body>
</html>
```